Etiketten-Design für Honig
Zielgruppe
Flinker Honig aus dem Bayerischen Wald
Bio
Waldhonig sowie Honig mit Zusätzen wie Bio-Himbeere, Bio-Erdbeere usw.
Aufgabenstellung
Bär, Bayrischer Wald, Bio Nr. und natürlich Honig
Modern und cool

```html
<!DOCTYPE html>
<html lang="de">
<head>
<meta charset="utf-8">
<title>Flinker Honig – Etiketten</title>
<link href="https://fonts.googleapis.com/css2?family=Quicksand:wght@600;700&family=Kaushan+Script&display=swap" rel="stylesheet">
<style>
  :root {
    --paper: #ffffff;
    --honey-light: #f4c552;
    --honey: #eeb03e;
    --honey-deep: #df912c;
    --ink: #231f20;
    --ribbon-text: #ffffff;
    --bear-brown: #6d4a2a;
    --bear-dark: #4a321c;
    --seal-fill: #fbe7b5;
  }
  html, body {
    margin: 0;
    padding: 0;
    overflow: hidden;
    background: var(--paper);
  }
  .canvas {
    position: relative;
    width: 1200px;
    height: 1140px;
    background: var(--paper);
    overflow: hidden;
  }
  .label {
    position: absolute;
    width: 372px;
    height: 742px;
  }
  .label--wald { left: 412px; top: 64px; }
  .label--erdbeer { left: 61px; top: 338px; }
  .label--himbeer { left: 763px; top: 338px; }
  .label__shape {
    position: absolute;
    inset: 0;
    width: 372px;
    height: 742px;
  }
  .tag-brand {
    position: absolute;
    left: 36px;
    top: 62px;
    width: 300px;
    text-align: center;
    font-family: "Quicksand", sans-serif;
    font-weight: 700;
    font-size: 52px;
    line-height: 56px;
    color: var(--ink);
    transform: rotate(-8deg);
  }
  .hex-brand {
    position: absolute;
    left: 30px;
    top: 406px;
    width: 312px;
    text-align: center;
    font-family: "Quicksand", sans-serif;
    font-weight: 700;
    font-size: 38px;
    line-height: 44px;
    color: var(--ink);
    transform: rotate(-6deg);
  }
  .ribbon-text {
    position: absolute;
    left: 60px;
    top: 472px;
    width: 252px;
    text-align: center;
    font-family: "Quicksand", sans-serif;
    font-weight: 700;
    font-size: 19px;
    line-height: 30px;
    color: var(--ribbon-text);
    transform: rotate(-5deg);
    white-space: nowrap;
  }
  .variety {
    position: absolute;
    left: 40px;
    top: 515px;
    width: 292px;
    text-align: center;
    font-family: "Kaushan Script", cursive;
    font-size: 34px;
    line-height: 42px;
    color: var(--ink);
    transform: rotate(-6deg);
  }
</style>
</head>
<body>
<main class="canvas">

  <article class="label label--wald">
    <svg class="label__shape" viewBox="0 0 372 742">
      <defs>
        <radialGradient id="honey-fill-wald" cx="50%" cy="50%" r="60%">
          <stop offset="0" stop-color="var(--honey-light)"/>
          <stop offset="0.6" stop-color="var(--honey)"/>
          <stop offset="1" stop-color="var(--honey-deep)"/>
        </radialGradient>
        <radialGradient id="bear-fill-wald" cx="50%" cy="45%" r="60%">
          <stop offset="0" stop-color="var(--bear-brown)"/>
          <stop offset="1" stop-color="var(--bear-dark)"/>
        </radialGradient>
      </defs>
      <g class="label__body" fill="url(#honey-fill-wald)" stroke="var(--ink)" stroke-width="7">
        <path d="M160 236 V340 L4 421 V633 L186 739 L368 633 V421 L212 340 V236"/>
        <circle cx="186" cy="124" r="119"/>
      </g>
      <rect x="164" y="236" width="44" height="110" fill="var(--honey-deep)"/>
      <g class="ribbon" transform="rotate(-5 186 487)" fill="var(--ink)">
        <polygon points="20,476 78,482 78,512 34,512 48,496"/>
        <polygon points="352,476 294,482 294,512 338,512 324,496"/>
        <rect x="60" y="470" width="252" height="34"/>
      </g>
      <rect class="bear-illustration" role="img" aria-label="Illustration eines schlafenden Braunbären, der ein Honigglas umarmt, zwischen Gräsern" x="96" y="576" width="184" height="116" rx="58" fill="url(#bear-fill-wald)"/>
      <circle class="seal-placeholder" cx="318" cy="596" r="24" fill="var(--seal-fill)"/>
    </svg>
    <div class="tag-brand">Flinker<br>Honig</div>
    <div class="hex-brand">Flinker Honig</div>
    <div class="ribbon-text">aus dem Bayerischen Wald</div>
    <div class="variety">Waldhonig</div>
  </article>

  <article class="label label--erdbeer">
    <svg class="label__shape" viewBox="0 0 372 742">
      <defs>
        <radialGradient id="honey-fill-erdbeer" cx="50%" cy="50%" r="60%">
          <stop offset="0" stop-color="var(--honey-light)"/>
          <stop offset="0.6" stop-color="var(--honey)"/>
          <stop offset="1" stop-color="var(--honey-deep)"/>
        </radialGradient>
        <radialGradient id="bear-fill-erdbeer" cx="50%" cy="45%" r="60%">
          <stop offset="0" stop-color="var(--bear-brown)"/>
          <stop offset="1" stop-color="var(--bear-dark)"/>
        </radialGradient>
      </defs>
      <g class="label__body" fill="url(#honey-fill-erdbeer)" stroke="var(--ink)" stroke-width="7">
        <path d="M160 236 V340 L4 421 V633 L186 739 L368 633 V421 L212 340 V236"/>
        <circle cx="186" cy="124" r="119"/>
      </g>
      <rect x="164" y="236" width="44" height="110" fill="var(--honey-deep)"/>
      <g class="ribbon" transform="rotate(-5 186 487)" fill="var(--ink)">
        <polygon points="20,476 78,482 78,512 34,512 48,496"/>
        <polygon points="352,476 294,482 294,512 338,512 324,496"/>
        <rect x="60" y="470" width="252" height="34"/>
      </g>
      <rect class="bear-illustration" role="img" aria-label="Illustration eines schlafenden Braunbären, der ein Honigglas umarmt, zwischen Gräsern" x="96" y="576" width="184" height="116" rx="58" fill="url(#bear-fill-erdbeer)"/>
      <circle class="seal-placeholder" cx="318" cy="596" r="24" fill="var(--seal-fill)"/>
    </svg>
    <div class="tag-brand">Flinker<br>Honig</div>
    <div class="hex-brand">Flinker Honig</div>
    <div class="ribbon-text">aus dem Bayerischen Wald</div>
    <div class="variety">Erdbeerhonig</div>
  </article>

  <article class="label label--himbeer">
    <svg class="label__shape" viewBox="0 0 372 742">
      <defs>
        <radialGradient id="honey-fill-himbeer" cx="50%" cy="50%" r="60%">
          <stop offset="0" stop-color="var(--honey-light)"/>
          <stop offset="0.6" stop-color="var(--honey)"/>
          <stop offset="1" stop-color="var(--honey-deep)"/>
        </radialGradient>
        <radialGradient id="bear-fill-himbeer" cx="50%" cy="45%" r="60%">
          <stop offset="0" stop-color="var(--bear-brown)"/>
          <stop offset="1" stop-color="var(--bear-dark)"/>
        </radialGradient>
      </defs>
      <g class="label__body" fill="url(#honey-fill-himbeer)" stroke="var(--ink)" stroke-width="7">
        <path d="M160 236 V340 L4 421 V633 L186 739 L368 633 V421 L212 340 V236"/>
        <circle cx="186" cy="124" r="119"/>
      </g>
      <rect x="164" y="236" width="44" height="110" fill="var(--honey-deep)"/>
      <g class="ribbon" transform="rotate(-5 186 487)" fill="var(--ink)">
        <polygon points="20,476 78,482 78,512 34,512 48,496"/>
        <polygon points="352,476 294,482 294,512 338,512 324,496"/>
        <rect x="60" y="470" width="252" height="34"/>
      </g>
      <rect class="bear-illustration" role="img" aria-label="Illustration eines schlafenden Braunbären, der ein Honigglas umarmt, zwischen Gräsern" x="96" y="576" width="184" height="116" rx="58" fill="url(#bear-fill-himbeer)"/>
      <circle class="seal-placeholder" cx="318" cy="596" r="24" fill="var(--seal-fill)"/>
    </svg>
    <div class="tag-brand">Flinker<br>Honig</div>
    <div class="hex-brand">Flinker Honig</div>
    <div class="ribbon-text">aus dem Bayerischen Wald</div>
    <div class="variety">Himbeerhonig</div>
  </article>

</main>
</body>
</html>
```